Stonevale Business Card Design

The Stonevale Co is an aggregate (crushing) equipment dealer serving Western Canadian provinces. Stonevale is a distributor of aggregate equipment for different manufacturers.

We are looking to change and update the existing business card which has been used since the existence of the company. A copy of existing card has been attached for reference. The Stonevale Co logo we want to remain the same and we want the green color to remain the same.

We are wanting something new with a different look. A refreshing card to show a new modern and updated look. No longer wanting to have the manufacturers on the back of the card but something more like our logo on the back of the card with a statement like "Crushing Solutions"

ideas could be:
- card can be different colors on front and back
- front or reverse of the card could possibly be the green color with the logo in black

Target Market(s)

Owners of Aggregate/Crushing companies

Contact Information for Business Card

see above

Requirements
Must have
• - logo to remain same along with same font within logo
• - green color to remain same
Nice to have
• as noted above under project description
Should not have

```html
<!DOCTYPE html>
<html lang="en">
<head>
<meta charset="utf-8">
<title>Stonevale Co — Business Card</title>
<link rel="stylesheet" href="https://fonts.googleapis.com/css2?family=Roboto:wght@400;500;700&display=swap">
<style>
  :root {
    --stage: #3b3b3d;
    --ink: #231f20;
    --olive: #868600;
    --olive-dark: #6f6f00;
    --olive-light: #949406;
    --paper: #ffffff;
    --text: #2a2a2a;
  }
  * { margin: 0; padding: 0; box-sizing: border-box; }
  html, body { width: 1200px; height: 900px; overflow: hidden; }
  body {
    background: var(--stage);
    font-family: "Roboto", Arial, sans-serif;
    position: relative;
  }
  .card {
    position: absolute;
    width: 514px;
    height: 296px;
    border-radius: 26px;
    overflow: hidden;
  }
  .card--dark { background: var(--ink); }
  .card--olive { background: var(--olive); }
  .card--paper { background: var(--paper); }

  .pos-tl { left: 73px; top: 138px; }
  .pos-tr { left: 615px; top: 138px; }
  .pos-bl { left: 73px; top: 464px; }
  .pos-br { left: 615px; top: 464px; }

  /* large brand decoration area on the dark faces */
  .brand-field {
    position: absolute;
    left: 0; right: 0;
    border-radius: 0 0 60px 60px;
    background: linear-gradient(100deg, var(--olive) 0%, var(--olive-dark) 50%, var(--olive) 100%);
    opacity: 0.9;
  }
  .pos-tl .brand-field { top: 32px; height: 190px; }
  .pos-tr .brand-field { top: 42px; height: 200px; }

  /* soft tonal backdrop on the olive face */
  .tone-field {
    position: absolute;
    inset: 0;
    background:
      radial-gradient(ellipse 60% 45% at 85% 20%, var(--olive-dark), transparent 70%),
      radial-gradient(ellipse 55% 40% at 60% 95%, var(--olive-dark), transparent 70%),
      radial-gradient(ellipse 45% 35% at 5% 85%, var(--olive-dark), transparent 70%),
      var(--olive);
  }

  /* wordmark placeholder */
  .wordmark {
    position: absolute;
    display: flex;
    align-items: center;
    gap: 10px;
    font-weight: 700;
    font-size: 24px;
    letter-spacing: 1px;
    white-space: nowrap;
  }
  .wordmark__dot {
    width: 26px; height: 26px;
    border-radius: 50%;
    flex: none;
  }
  .card--olive .wordmark {
    left: 0; right: 0; top: 112px;
    justify-content: center;
    color: var(--ink);
  }
  .card--olive .wordmark__dot { background: var(--ink); }
  .card--paper .wordmark {
    left: 62px; top: 108px;
    color: var(--olive);
  }
  .card--paper .wordmark__dot { background: var(--olive); }

  .company-name {
    position: absolute;
    font-weight: 700;
    letter-spacing: 0.2px;
    white-space: nowrap;
  }
  .card--dark .company-name {
    left: 42px; top: 250px;
    color: var(--paper);
    font-size: 14px;
  }
  .card--olive .company-name {
    left: 0; right: 0; top: 186px;
    text-align: center;
    color: var(--ink);
    font-size: 16px;
  }
  .card--paper .company-name {
    left: 47px; top: 182px;
    color: var(--ink);
    font-size: 16px;
  }

  .divider {
    position: absolute;
    left: 283px; top: 56px;
    width: 6px; height: 180px;
    border-left: 2px solid var(--olive);
    border-right: 2px solid var(--olive);
  }
  .contact {
    position: absolute;
    left: 324px; top: 68px;
    color: var(--text);
  }
  .contact__name {
    color: var(--olive);
    font-weight: 500;
    font-size: 17px;
    margin-bottom: 8px;
  }
  .contact__group { margin-bottom: 9px; }
  .contact__line {
    display: flex;
    align-items: flex-start;
    font-size: 12px;
    line-height: 14.5px;
  }
  .contact__line svg {
    width: 10px; height: 10px;
    margin: 2px 6px 0 0;
    flex: none;
  }

  .tagline-band {
    position: absolute;
    left: 0; right: 0; bottom: 0;
    height: 39px;
    background: var(--olive);
    color: var(--paper);
    font-size: 15px;
    letter-spacing: 3.6px;
    display: flex;
    align-items: center;
    justify-content: center;
    white-space: nowrap;
  }
</style>
</head>
<body>

  <section class="card card--dark pos-tl">
    <div class="brand-field" role="img" aria-label="Large olive brand symbol decoration across the card face"></div>
    <p class="company-name">THE STONEVALE CO.</p>
  </section>

  <section class="card card--dark pos-tr">
    <div class="brand-field" role="img" aria-label="Large olive brand symbol decoration across the card face"></div>
  </section>

  <section class="card card--olive pos-bl">
    <div class="tone-field" role="img" aria-label="Soft tonal olive backdrop shapes"></div>
    <div class="wordmark"><span class="wordmark__dot"></span>STONEVALE</div>
    <p class="company-name">THE STONEVALE CO.</p>
  </section>

  <section class="card card--paper pos-br">
    <div class="wordmark"><span class="wordmark__dot"></span>STONEVALE</div>
    <p class="company-name">THE STONEVALE CO.</p>
    <div class="divider"></div>

    <div class="contact">
      <p class="contact__name">DALE MARSH</p>

      <div class="contact__group">
        <p class="contact__line">
          <svg viewBox="0 0 10 10"><circle cx="5" cy="5" r="4.3" fill="none" stroke="var(--olive)" stroke-width="1"/><rect x="3.6" y="2.4" width="2.8" height="5.2" rx="0.6" fill="var(--olive)"/></svg>
          780 555 0142
        </p>
        <p class="contact__line">
          <svg viewBox="0 0 10 10"><circle cx="5" cy="5" r="4.3" fill="none" stroke="var(--olive)" stroke-width="1"/><path d="M2.6 4.2h4.8v2.6H2.6z" fill="var(--olive)"/></svg>
          780 555 0187
        </p>
        <p class="contact__line">
          <svg viewBox="0 0 10 10"><circle cx="5" cy="5" r="5" fill="var(--olive)"/><path d="M3 3.2c.4 1.8 1.6 3.2 3.8 3.8l.6-.9-1-.6-.5.5c-.8-.4-1.4-1-1.7-1.8l.5-.5-.6-1z" fill="var(--paper)"/></svg>
          780 555 0163
        </p>
      </div>

      <div class="contact__group">
        <p class="contact__line">
          <svg viewBox="0 0 10 10"><circle cx="5" cy="5" r="5" fill="var(--olive)"/><path d="M2.5 3.4h5v3.2h-5z M2.5 3.4L5 5.3 7.5 3.4" fill="none" stroke="var(--paper)" stroke-width="0.8"/></svg>
          dale@stonevale.com
        </p>
        <p class="contact__line">
          <svg viewBox="0 0 10 10"><circle cx="5" cy="5" r="5" fill="var(--olive)"/><circle cx="5" cy="5" r="2.7" fill="none" stroke="var(--paper)" stroke-width="0.7"/><path d="M2.3 5h5.4M5 2.3v5.4" stroke="var(--paper)" stroke-width="0.6"/></svg>
          www.stonevale.ca
        </p>
      </div>

      <div class="contact__group">
        <p class="contact__line">
          <svg viewBox="0 0 10 10"><circle cx="5" cy="5" r="4.3" fill="none" stroke="var(--olive)" stroke-width="1"/><path d="M5 2.2a1.8 1.8 0 0 1 1.8 1.8C6.8 5.4 5 7.6 5 7.6S3.2 5.4 3.2 4A1.8 1.8 0 0 1 5 2.2z" fill="var(--olive)"/></svg>
          <span>2210 - 48B Street<br>Camrose, AB T4V 1K9</span>
        </p>
      </div>
    </div>

    <div class="tagline-band">SCREENERS | CRUSHERS | STACKERS</div>
  </section>

</body>
</html>
```